Company or website name
- LORAVEX
- Links to the website
- WWW.LORAVEX.NET
- Describe your company and organization and target audience
- check the website: www.loravex.net
- The design should have the following
- A clean visual is expected. The documents should include the complete address, emails, phone, name and position.
- Other Facts

```html
<!DOCTYPE html>
<html lang="en">
<head>
<meta charset="utf-8">
<title>LORAVEX Business Card</title>
<link rel="stylesheet" href="https://fonts.googleapis.com/css2?family=Montserrat:wght@300;400;500;600&family=Open+Sans:wght@400;600&display=swap">
<style>
  :root {
    --navy: #0e2f57;
    --teal: #56bfd3;
    --paper: #f2f3f4;
    --ink: #3a3f45;
    --bg: #e9e6e3;
    --white: #ffffff;
  }
  * { margin: 0; padding: 0; box-sizing: border-box; }
  html, body { width: 1200px; height: 944px; overflow: hidden; background: var(--bg); }
  .canvas {
    width: 1200px; height: 944px;
    display: flex; flex-direction: column; align-items: center; justify-content: center; gap: 56px;
  }
  .card {
    width: 630px; height: 360px; position: relative; overflow: hidden;
    box-shadow: 0 6px 18px rgba(0,0,0,0.12);
  }
  /* Front */
  .card-front {
    background: var(--navy);
    display: flex; flex-direction: column; align-items: center; justify-content: center;
  }
  .front-name {
    font-family: "Montserrat", sans-serif; font-weight: 400;
    font-size: 74px; letter-spacing: 3px; color: var(--white);
    margin-top: 10px;
  }
  .front-web {
    font-family: "Montserrat", sans-serif; font-weight: 400;
    font-size: 13px; letter-spacing: 4px; color: #cdd6e2;
    margin-top: 46px;
  }
  /* Back */
  .card-back { background: var(--paper); }
  .back-title {
    position: absolute; left: 0; right: 0; top: 96px; text-align: center;
    font-family: "Montserrat", sans-serif; font-size: 31px; font-weight: 600;
    letter-spacing: 0.5px;
  }
  .back-title .company { color: var(--navy); }
  .back-title .division { color: var(--teal); font-weight: 500; }
  .band {
    position: absolute; left: 0; right: 0; top: 150px; height: 150px;
    background: var(--navy);
    border-bottom: 4px solid var(--teal);
  }
  .person {
    position: absolute; left: 48px; top: 76px; text-align: right;
    font-family: "Open Sans", sans-serif; color: var(--white);
  }
  .person-name { font-size: 23px; font-weight: 600; line-height: 1.1; }
  .person-role { font-size: 13px; color: #c7d2de; }
  .divider {
    position: absolute; left: 270px; top: 22px; width: 1px; height: 106px;
    background: rgba(255,255,255,0.45);
  }
  .contacts {
    position: absolute; left: 292px; top: 24px; list-style: none;
    font-family: "Open Sans", sans-serif; font-size: 14px; color: var(--white);
  }
  .contacts li { display: flex; align-items: center; gap: 9px; height: 24px; }
  .contacts svg { width: 14px; height: 14px; flex: none; }
  .address {
    position: absolute; right: 40px; bottom: 22px;
    font-family: "Open Sans", sans-serif; font-size: 14px; color: var(--ink);
  }
</style>
</head>
<body>
<main class="canvas">
  <section class="card card-front">
    <div class="front-name">LORAVEX</div>
    <div class="front-web">www.loravex.net</div>
  </section>

  <section class="card card-back">
    <h1 class="back-title"><span class="company">LORAVEX</span> <span class="division">DRILLING SUPPLIES</span></h1>
    <div class="band">
      <div class="person">
        <div class="person-name">Dario Quintell</div>
        <div class="person-role">President</div>
      </div>
      <div class="divider"></div>
      <ul class="contacts">
        <li>
          <svg viewBox="0 0 16 16" aria-hidden="true"><path fill="#fff" d="M3.5 1.5l2.5 0 1 3.5-1.6 1.2c.8 1.8 2.2 3.2 4 4l1.2-1.6 3.4 1v2.5c0 .8-.7 1.5-1.5 1.5C6.7 13.6 2.4 9.3 2 3c0-.8.7-1.5 1.5-1.5z"/></svg>
          +507 614-2270
        </li>
        <li>
          <svg viewBox="0 0 16 16" aria-hidden="true"><rect x="4" y="1" width="8" height="14" rx="1.5" fill="none" stroke="#fff" stroke-width="1.5"/><circle cx="8" cy="12.5" r="0.9" fill="#fff"/></svg>
          +507 6380-4417
        </li>
        <li>
          <svg viewBox="0 0 16 16" aria-hidden="true"><rect x="1.5" y="3.5" width="13" height="9" fill="none" stroke="#fff" stroke-width="1.4"/><path d="M1.5 3.5L8 9l6.5-5.5" fill="none" stroke="#fff" stroke-width="1.4"/></svg>
          sales@loravex.net
        </li>
        <li>
          <svg viewBox="0 0 16 16" aria-hidden="true"><circle cx="8" cy="8" r="6.5" fill="none" stroke="#fff" stroke-width="1.3"/><ellipse cx="8" cy="8" rx="2.8" ry="6.5" fill="none" stroke="#fff" stroke-width="1.1"/><path d="M1.5 8h13" stroke="#fff" stroke-width="1.1"/></svg>
          www.loravex.net
        </li>
      </ul>
    </div>
    <p class="address">Calle Brisas, Lomas del Mar Ciudad Costera</p>
  </section>
</main>
</body>
</html>
```